Property Developer Business card design

we need a business card design + printing for a new Property developer company based in melbourne.
We are a group of investors investing in a property developer business. We have more projects involved in residential property as opposed to commercial property but we are involved in both market. we also provide consulting services with overseas investors willing to invest in the australian property market.
Updates
I have uploaded the logo. I'm not very convince with the colors of my logo... any suggestion please?.
Thanks guys!
Target Market(s)
property investors or person willing to purchase investment property
Industry/Entity Type
Residential
Contact Information for Business Card
Tallgrove Holdings Australia Pty Ltd
Look and feel
Each slider illustrates characteristics of the customer's brand and the style your logo design should communicate.

```html
<!DOCTYPE html>
<html lang="en">
<head>
<meta charset="utf-8">
<title>Tallgrove Holdings Australia – Business Card</title>
<link rel="stylesheet" href="https://fonts.googleapis.com/css2?family=Didact+Gothic&display=swap">
<style>
  :root {
    --page: #e7e4e0;
    --card-black: #141414;
    --brand-blue: #2f80f5;
    --text-blue: #1f86f0;
    --white: #ffffff;
    --font: "Didact Gothic", "Century Gothic", sans-serif;
  }
  * { box-sizing: border-box; margin: 0; padding: 0; }
  html, body {
    width: 1200px; height: 1000px; overflow: hidden;
    background: var(--page); font-family: var(--font);
  }
  .canvas { position: relative; width: 1200px; height: 1000px; }
  .card {
    position: absolute; left: 210px; width: 780px; height: 430px;
    background: var(--card-black); overflow: hidden;
    border-radius: 44px 10px 44px 0;
    box-shadow: 0 6px 18px rgba(0,0,0,.18);
  }
  .card-front { top: 50px; }
  .card-back { top: 520px; }
  .wave { position: absolute; inset: 0; width: 100%; height: 100%; }

  .brand { position: absolute; display: flex; align-items: center; color: var(--text-blue); }
  .brand-mark { background: var(--white); }
  .card-front .brand { left: 36px; top: 36px; gap: 12px; font-size: 27px; }
  .card-front .brand-mark { width: 26px; height: 26px; }
  .card-back .brand { left: 0; right: 0; top: 170px; justify-content: center; gap: 20px; font-size: 50px; }
  .card-back .brand-mark { width: 56px; height: 56px; }

  .holder { position: absolute; right: 70px; top: 100px; text-align: right; color: var(--white); }
  .holder-name { font-size: 50px; line-height: 1; letter-spacing: .5px; }
  .holder-title { font-size: 15px; margin-top: 8px; }

  .contacts {
    position: absolute; left: 40px; bottom: 30px; list-style: none;
    color: var(--white); font-size: 12.5px; letter-spacing: 2px; line-height: 1.35;
  }
  .contacts li { display: flex; align-items: center; gap: 8px; }
  .contacts svg { width: 10px; height: 11px; fill: var(--white); }
</style>
</head>
<body>
<main class="canvas">
  <section class="card card-front" aria-label="Business card front">
    <svg class="wave" viewBox="0 0 780 430" preserveAspectRatio="none" aria-hidden="true">
      <path d="M0 235 C60 150 140 130 300 175 C460 220 540 275 640 235 C720 200 760 110 780 40 L780 430 L0 430 Z" fill="var(--white)"/>
      <path d="M0 250 C60 165 140 145 300 190 C460 235 540 290 640 250 C720 215 765 125 780 58 L780 430 L0 430 Z" fill="var(--brand-blue)"/>
    </svg>
    <div class="brand"><span class="brand-mark"></span><span class="brand-name">Tallgrove Holdings Australia</span></div>
    <div class="holder">
      <p class="holder-name">Daniel Marsh</p>
      <p class="holder-title">Managing Director</p>
    </div>
    <ul class="contacts">
      <li><svg viewBox="0 0 10 11"><rect x="2" y="0" width="6" height="11" rx="1"/></svg>0400 555 218</li>
      <li><svg viewBox="0 0 10 11"><path d="M1 1 L4 1 L5 4 L3 5 Q4 7 6 8 L7 6 L10 7 L10 10 Q4 11 0 4 Z"/></svg>+61 3 9000 5126</li>
      <li><svg viewBox="0 0 10 11"><rect x="0" y="2" width="10" height="7" rx="1"/></svg>daniel.marsh@tallgrove.com.au</li>
      <li><svg viewBox="0 0 10 11"><rect x="1" y="1" width="8" height="10" rx="4"/></svg>www.tallgroveholdings.com</li>
    </ul>
  </section>

  <section class="card card-back" aria-label="Business card back">
    <div class="brand"><span class="brand-mark"></span><span class="brand-name">Tallgrove Holdings Australia</span></div>
  </section>
</main>
</body>
</html>
```